Progressive/contemporary business card design for successful Startups as a Service Company

New logo launched in 2020. New website launched in 2021. Now that COVID is (mostly) behind us, I'm networking with more people and need a business card that matches the company/logo design aesthetic.

```html
<!DOCTYPE html>
<html lang="en">
<head>
<meta charset="utf-8">
<title>Brightpath Business Card</title>
<link rel="stylesheet" href="https://fonts.googleapis.com/css2?family=Montserrat:wght@400;500;700&display=swap">
<style>
  :root {
    --backdrop: #1b1b1b;
    --card: #2b2a2a;
    --white: #f2f2f2;
    --blue: #1a7bcc;
    --red: #e8381f;
    --green: #3fa845;
    --purple: #8a2597;
    --name-blue: #1a7fd0;
    --icon-red: #e5372a;
  }
  * { margin: 0; padding: 0; box-sizing: border-box; }
  html, body { width: 1200px; height: 1021px; overflow: hidden; }
  body {
    background: var(--backdrop);
    font-family: "Montserrat", sans-serif;
    position: relative;
  }
  .card {
    position: absolute;
    left: 250px;
    width: 700px;
    height: 400px;
    background: var(--card);
    overflow: hidden;
    box-shadow: 0 10px 30px rgba(0,0,0,0.45);
  }
  .card--front { top: 80px; }
  .card--back { top: 541px; }

  .accent-band {
    position: absolute;
    left: 0; right: 0; bottom: 0;
    height: 14px;
    background: linear-gradient(90deg, var(--blue), var(--red), var(--green), var(--purple));
  }

  .wordmark {
    display: flex;
    align-items: center;
    gap: 14px;
    color: var(--white);
    font-weight: 500;
    letter-spacing: 0.32em;
    line-height: 1;
  }
  .wordmark__square {
    width: 26px; height: 26px;
    background: var(--blue);
    flex: none;
  }
  .card--front .wordmark {
    position: absolute;
    left: 0; right: 0; top: 168px;
    justify-content: center;
    font-size: 38px;
  }
  .card--back .wordmark {
    position: absolute;
    left: 46px; top: 44px;
    font-size: 30px;
  }
  .card--back .wordmark__square { width: 22px; height: 22px; }

  .accent-rule {
    position: absolute;
    left: 150px; top: 184px;
    width: 290px; height: 1.5px;
    background: linear-gradient(90deg, var(--blue), var(--red), var(--green), var(--purple));
  }

  .contact-list {
    position: absolute;
    left: 46px; top: 256px;
    list-style: none;
    color: var(--white);
    font-size: 17px;
    line-height: 27px;
  }
  .contact-list li { display: flex; align-items: center; gap: 9px; }
  .contact-list svg { width: 15px; height: 15px; flex: none; }

  .person {
    position: absolute;
    left: 448px; top: 196px;
    width: 230px;
  }
  .person__name {
    color: var(--name-blue);
    font-weight: 700;
    font-size: 25px;
    line-height: 1.1;
  }
  .person__title {
    color: var(--white);
    font-size: 17px;
    margin-top: 4px;
    padding-left: 16px;
  }
  .address {
    position: absolute;
    left: 440px; top: 290px;
    width: 240px;
    color: var(--white);
    font-size: 17px;
    line-height: 26px;
    font-style: normal;
  }
</style>
</head>
<body>

<section class="card card--front" aria-label="Card front">
  <div class="wordmark"><span class="wordmark__text">BRIGHTPATH</span><span class="wordmark__square"></span></div>
  <div class="accent-band" role="img" aria-label="Multicolour accent band in blue, red, green and purple"></div>
</section>

<section class="card card--back" aria-label="Card back">
  <div class="wordmark"><span class="wordmark__text">BRIGHTPATH</span><span class="wordmark__square"></span></div>
  <div class="accent-rule" role="img" aria-label="Thin multicolour accent rule"></div>

  <ul class="contact-list">
    <li>
      <svg viewBox="0 0 16 16" aria-hidden="true"><path d="M4 1.5l2.2 2.8-1.3 1.6c.8 1.9 2.3 3.4 4.2 4.2l1.6-1.3 2.8 2.2-1.4 2.5C7 13.3 2.7 9 1.5 3z" fill="none" stroke="var(--icon-red)" stroke-width="1.5" stroke-linejoin="round"/></svg>
      (555) 014-2278
    </li>
    <li>
      <svg viewBox="0 0 16 16" aria-hidden="true"><rect x="1.5" y="3.5" width="13" height="9" fill="none" stroke="var(--icon-red)" stroke-width="1.5"/><path d="M1.5 3.5L8 9l6.5-5.5" fill="none" stroke="var(--icon-red)" stroke-width="1.5"/></svg>
      daniel@brightpathlabs.com
    </li>
    <li>
      <svg viewBox="0 0 16 16" aria-hidden="true"><g fill="none" stroke="var(--icon-red)" stroke-width="1.3"><circle cx="8" cy="8" r="6.5"/><ellipse cx="8" cy="8" rx="3" ry="6.5"/><path d="M1.5 8h13M2.6 4.5h10.8M2.6 11.5h10.8"/></g></svg>
      www.brightpathlabs.com
    </li>
  </ul>

  <div class="person">
    <p class="person__name">Daniel Reyes</p>
    <p class="person__title">Managing Director</p>
  </div>

  <address class="address">
    418 Harbor Street<br>
    Coral Bay, Florida, 33190
  </address>

  <div class="accent-band" role="img" aria-label="Multicolour accent band in blue, red, green and purple"></div>
</section>

</body>
</html>
```